Apartments rental business needs a web for direct reservations.

I need a website that allows my clients to check the property (pictures, a brief description etc) and lets them make reservations. They will be providing the required information such as name, last name, email address and credit card details. Also a calendar where I can update the availability (dates and prices) of the property upon new reservations is a must. I already have a logo that should also be a good starting point for colors, style an inspiration.

```html
<!DOCTYPE html>
<html lang="en">
<head>
<meta charset="utf-8">
<title>Solana Bungalows</title>
<link href="https://fonts.googleapis.com/css2?family=Lato:wght@300;400;700;900&display=swap" rel="stylesheet">
<style>
:root{
  --teal:#2bb5a0;
  --teal-dark:#1f9c88;
  --orange:#ea5a24;
  --ink:#333;
  --muted:#555;
  --white:#fff;
  --line:#c9c9c9;
}
*{box-sizing:border-box;margin:0;padding:0}
html,body{width:1200px;height:3237px;overflow:hidden}
body{position:relative;font-family:'Lato',sans-serif;color:var(--ink);background:var(--white)}
.abs{position:absolute}
/* header */
.site-header{position:absolute;left:0;top:0;width:1200px;height:97px;background:var(--white);z-index:2}
.nav a{position:absolute;top:38px;font-size:17px;color:#222;text-decoration:none;text-transform:uppercase;letter-spacing:.3px}
.nav a.active{color:var(--teal)}
.brand-tab{position:absolute;left:469px;top:0;width:262px;height:155px;background:var(--white);border-radius:0 0 60px 60px;z-index:3;text-align:center}
.brand-mark{display:block;width:64px;height:64px;border-radius:50%;background:var(--teal);margin:16px auto 12px}
.brand-name{font-size:20px;font-weight:700;color:var(--orange);letter-spacing:.5px;text-transform:uppercase;white-space:nowrap}
/* hero */
.hero{position:absolute;left:0;top:97px;width:1200px;height:637px;background:linear-gradient(180deg,#5f86c9 0%,#8aa6d4 25%,#7a4a3a 55%,#6e6a58 80%,#4d6b36 100%)}
.hero-title{position:absolute;left:0;width:1200px;text-align:center;color:var(--white);white-space:nowrap}
.hero-title.light{top:214px;font-weight:300;font-size:50px;letter-spacing:1px;line-height:60px}
.hero-title.bold{top:266px;font-weight:700;font-size:54px;line-height:64px}
.btn{position:absolute;display:flex;align-items:center;justify-content:center;border-radius:28px;color:var(--white);font-weight:700;font-size:18px;text-transform:uppercase}
.btn-orange{background:var(--orange)}
.btn-teal{background:var(--teal)}
/* about */
.about-photo{left:162px;top:820px;width:360px;height:330px;border-radius:50%;background:linear-gradient(180deg,#3f6b3a 0%,#5a8a55 40%,#7cc0d8 55%,#8a6a55 75%,#6d4c3b 100%)}
.section-title{font-weight:700;text-transform:uppercase;font-size:35px}
.section-title .teal{color:var(--teal)}
.section-title .orange{color:var(--orange)}
.about-text{left:585px;width:500px;font-size:16px;line-height:24px;color:var(--ink)}
/* facilities */
.facilities{left:0;top:1239px;width:604px;height:516px;background:var(--orange);color:var(--white)}
.facilities-photo{left:604px;top:1239px;width:596px;height:516px;background:linear-gradient(135deg,#e9e7e2 0%,#cfccc5 45%,#6a6a6c 70%,#b8322a 85%,#d8d4cd 100%)}
.facilities h2{position:absolute;left:168px;top:95px;font-size:28px;font-weight:700;text-transform:uppercase;white-space:nowrap}
.facilities p{position:absolute;left:168px;top:148px;width:404px;font-size:15.5px;line-height:24px}
.features{position:absolute;left:168px;top:318px;width:400px;list-style:none;display:grid;grid-template-columns:186px 200px;row-gap:11px}
.features li{font-size:15px;font-weight:700;display:flex;align-items:center;gap:6px}
/* gallery */
.gallery-grid{left:132px;top:1923px;width:925px;height:444px;display:grid;grid-template-columns:repeat(4,1fr);grid-template-rows:1fr 1fr;gap:2px}
.g1{background:linear-gradient(160deg,#d9d6cf,#8a8986 60%,#b7332b)}
.g2{grid-row:span 2;background:linear-gradient(180deg,#7fa6d8,#b0317f 35%,#3f6d2c 70%,#6b4a36)}
.g3{grid-column:span 2;background:linear-gradient(135deg,#ece9e3,#cfcac0 50%,#5b5b5e 75%,#c33b30)}
.g4{background:linear-gradient(180deg,#3d5a2a,#6c8f3d 60%,#2c3a22)}
.g5{background:linear-gradient(180deg,#e8e6e1,#bdb9b1 60%,#6d6a66)}
.g6{background:linear-gradient(180deg,#a39a8f,#efeeeb 55%,#23408a 80%,#ddd)}
/* reservation */
.reservation{left:0;top:2450px;width:1200px;height:420px;background:linear-gradient(180deg,rgba(43,181,160,.92),rgba(31,156,136,.95)),linear-gradient(90deg,#5a7a60,#2a6050)}
.reservation h2{position:absolute;left:0;top:66px;width:1200px;text-align:center;color:var(--white);font-size:34px;font-weight:700;text-transform:uppercase}
.field{position:absolute;height:47px;background:var(--white);display:flex;align-items:center;padding-left:18px;font-size:14.5px;color:#444;gap:10px}
.submit{position:absolute;height:47px;background:var(--orange);color:var(--white);font-size:19px;font-weight:700;display:flex;align-items:center;justify-content:center;text-transform:uppercase}
/* footer */
.footer-brand{left:153px;top:2935px;width:223px;text-align:center}
.footer-brand .brand-mark{width:70px;height:70px;margin:0 auto 14px}
.footer-h{font-size:16px;font-weight:700;color:var(--orange);text-transform:uppercase}
.footer-text{font-size:16.5px;line-height:26px;color:#444}
.social{display:flex;gap:7px}
.social span{width:34px;height:34px;border:1.5px solid var(--teal);border-radius:50%}
.links{list-style:none;font-size:16.5px;line-height:25px;color:#444}
.rule{left:162px;top:3175px;width:876px;height:1px;background:var(--line)}
.copyright{left:0;top:3194px;width:1200px;text-align:center;font-size:13.5px;color:#555}
</style>
</head>
<body>

<header class="site-header">
  <nav class="nav">
    <a class="active" style="left:168px">Home</a>
    <a style="left:248px">About Us</a>
    <a style="left:360px">Services</a>
    <a style="left:749px">Gallery</a>
    <a style="left:850px">Book Now</a>
    <a style="left:978px">Contact</a>
  </nav>
</header>
<div class="brand-tab">
  <span class="brand-mark"></span>
  <div class="brand-name">Solana Bungalows</div>
</div>

<section class="hero" role="img" aria-label="Photo of a white bungalow with a covered terrace, sun loungers and palm leaves under a blue sky">
  <h1 class="hero-title light">WELCOME TO</h1>
  <div class="hero-title bold">SOLANA BUNGALOWS</div>
  <div class="btn btn-orange" style="left:520px;top:348px;width:199px;height:54px">Book Now</div>
</section>

<section class="about">
  <div class="abs about-photo" role="img" aria-label="Photo of the garden swimming pool surrounded by trees"></div>
  <h2 class="abs section-title" style="left:585px;top:826px"><span class="teal">About</span> <span class="orange">Our Bungalows</span></h2>
  <p class="abs about-text" style="top:889px">Offering garden views, Solana Bungalows 45 &amp; 46 is an accommodation set in Playa Serena, 4.1 km from Ondalia Water Park and 3.8 km from Punta Clara Lighthouse. The accommodation is 12 km from the Verdemar Gardens.</p>
  <p class="abs about-text" style="top:1010px">The apartment features 2 bedrooms, a living room with a flat-screen TV, an equipped kitchen, and 1 bathroom with a shower.</p>
  <div class="btn btn-teal" style="left:585px;top:1090px;width:177px;height:49px">Read More</div>
</section>

<section class="abs facilities">
  <h2>Most Popular Facilities</h2>
  <p>Solana Bungalows are located inside a picturesque complex well known for its peaceful and quiet ambient. This single story bungalow is very comfortable and very well equipped with 2 bedrooms, a bathroom with hair dryer and a Living/dinning room with views to the private garden.</p>
  <ul class="features">
    <li><svg width="9" height="12" viewBox="0 0 9 12"><path d="M2 1l5 5-5 5" fill="none" stroke="#fff" stroke-width="2.2"/></svg>Swimming pool</li>
    <li><svg width="9" height="12" viewBox="0 0 9 12"><path d="M2 1l5 5-5 5" fill="none" stroke="#fff" stroke-width="2.2"/></svg>Outdoor pool</li>
    <li><svg width="9" height="12" viewBox="0 0 9 12"><path d="M2 1l5 5-5 5" fill="none" stroke="#fff" stroke-width="2.2"/></svg>Free WiFi</li>
    <li><svg width="9" height="12" viewBox="0 0 9 12"><path d="M2 1l5 5-5 5" fill="none" stroke="#fff" stroke-width="2.2"/></svg>Non-smoking rooms</li>
    <li><svg width="9" height="12" viewBox="0 0 9 12"><path d="M2 1l5 5-5 5" fill="none" stroke="#fff" stroke-width="2.2"/></svg>Free parking</li>
    <li><svg width="9" height="12" viewBox="0 0 9 12"><path d="M2 1l5 5-5 5" fill="none" stroke="#fff" stroke-width="2.2"/></svg>Terrace</li>
  </ul>
</section>
<div class="abs facilities-photo" role="img" aria-label="Photo of the living room with grey sofa, red armchair, framed line drawings and a view to the kitchen"></div>

<section class="gallery">
  <h2 class="abs section-title" style="left:0;top:1849px;width:1200px;text-align:center;font-size:34px"><span class="teal">Our Gallery</span></h2>
  <div class="abs gallery-grid">
    <div class="g1" role="img" aria-label="Photo of the sofa with red cushions and framed drawings"></div>
    <div class="g2" role="img" aria-label="Photo of pink bougainvillea over a garden pillar"></div>
    <div class="g3" role="img" aria-label="Photo of the open living and dining area"></div>
    <div class="g4" role="img" aria-label="Photo of sun loungers on the garden lawn"></div>
    <div class="g5" role="img" aria-label="Photo of the hallway towards the kitchen"></div>
    <div class="g6" role="img" aria-label="Photo of the bedroom with a double bed and blue towels"></div>
  </div>
</section>

<section class="abs reservation" role="img" aria-label="Faint photo of the terrace and palm trees behind the reservation form">
  <h2>Reservation Form</h2>
  <div class="field" style="left:214px;top:142px;width:250px">First Name</div>
  <div class="field" style="left:473px;top:142px;width:250px">Last Name</div>
  <div class="field" style="left:734px;top:142px;width:250px">Email address</div>
  <div class="field" style="left:214px;top:205px;width:250px">Card Type</div>
  <div class="field" style="left:473px;top:205px;width:511px">Card Number</div>
  <div class="field" style="left:214px;top:269px;width:250px">
    <svg width="17" height="17" viewBox="0 0 17 17"><rect x="1.5" y="3" width="14" height="12.5" rx="1.5" fill="none" stroke="var(--teal)" stroke-width="1.5"/><path d="M1.5 7h14M5 1v4M12 1v4" stroke="var(--teal)" stroke-width="1.5"/></svg>Date</div>
  <div class="field" style="left:473px;top:269px;width:250px">Price</div>
  <div class="submit" style="left:734px;top:269px;width:250px">Book Now</div>
</section>

<footer>
  <div class="abs footer-brand">
    <span class="brand-mark"></span>
    <div class="brand-name">Solana Bungalows</div>
  </div>
  <h3 class="abs footer-h" style="left:432px;top:2940px">Our Address</h3>
  <p class="abs footer-text" style="left:432px;top:2974px">22 Calle del Palmeral,<br>35990 Playa Serena, Spain</p>
  <div class="abs social" style="left:436px;top:3045px"><span></span><span></span><span></span><span></span></div>
  <h3 class="abs footer-h" style="left:729px;top:2937px">Quick Links</h3>
  <ul class="abs links" style="left:733px;top:2966px"><li>Home</li><li>About Us</li><li>Our Gallery</li><li>Book Now</li></ul>
  <ul class="abs links" style="left:876px;top:2962px"><li>Testimonials</li><li>Facilities</li><li>Contact Us</li></ul>
  <div class="abs rule"></div>
  <p class="abs copyright">© 2019 Company Name &nbsp;All right reserved</p>
</footer>

</body>
</html>
```